Bright Harbour Mortgages Social Media Campaign

I need social media campaign banners. Facebook and Instagram.
I would like them to incorporate local photos, my photo and my logo. I have some sample files of previous campaigns and I have a color scheme associated with my brand. My business operates in St. John's Newfoundland.

Target Market(s)

Home Buyers, Home Owners

Industry/Entity Type

Mortgage Brokering

Logo Text

Bright Harbour Mortgages

Logo styles of interest
Lettermark Logo
Font styles to use
Other font styles liked:
• Times New Roman, I'm open to suggestion

Colors
0054AA
0677BA
7BADD7
CADEEF
E8F1F8
EE7325
F08F49
F5BC92
FAE3D3
FDF4ED

Requirements
Must have
• My name, photo, contact info, slogan
Nice to have
• We can discuss slogans to use, I can provide some suggestions.

```html
<!DOCTYPE html>
<html lang="en">
<head>
<meta charset="utf-8">
<title>Bright Harbour Mortgages – Social Banners</title>
<link rel="stylesheet" href="https://fonts.googleapis.com/css2?family=Montserrat:wght@300;400;500;600;700;800;900&display=swap">
<style>
  :root {
    --backdrop: #d9d5d3;
    --navy: #0b1752;
    --orange: #fb4a0b;
    --ink: #1c1612;
    --panel-grey: #e2e2e5;
    --white: #ffffff;
    --black: #0c0c0c;
    --sky-top: #b9bcc6;
    --town-mid: #8d8a8e;
    --town-low: #8a5a52;
  }
  * { box-sizing: border-box; margin: 0; padding: 0; }
  html, body { width: 802px; height: 1200px; overflow: hidden; }
  body {
    background: var(--backdrop);
    font-family: "Montserrat", Arial, sans-serif;
    position: relative;
  }
  .banner {
    position: absolute;
    left: 111px;
    width: 580px;
    overflow: hidden;
    background: var(--white);
  }
  .banner--square { top: 123px; height: 580px; }
  .banner--wide { top: 774px; height: 304px; }
  .abs { position: absolute; }

  .town-photo {
    background: linear-gradient(180deg, var(--sky-top) 0%, #c9cbd1 35%, var(--town-mid) 60%, #9d7b6e 80%, var(--town-low) 100%);
  }
  .agent-photo {
    background: linear-gradient(180deg, #e6e6e8 0%, #d8c6b4 35%, #c59a72 55%, #1c2a4a 80%, #17223f 100%);
  }
  .grey-panel { background: var(--panel-grey); }
  .navy-band { background: var(--navy); }
  .roof { position: absolute; left: 0; top: 0; }

  .name-bar {
    background: var(--black);
    color: var(--white);
    font-weight: 700;
    text-align: center;
    letter-spacing: 0.2px;
  }
  .contact-card {
    background: var(--orange);
    border-radius: 0 0 10px 10px;
    display: flex;
    flex-direction: column;
    align-items: center;
    justify-content: space-around;
  }
  .contact-icon { display: block; }
  .contact-phone { color: var(--navy); font-weight: 800; }
  .contact-text { color: var(--white); font-weight: 600; }

  .brand {
    color: var(--orange);
    font-weight: 800;
    text-transform: uppercase;
    display: flex;
    align-items: center;
    gap: 7px;
    white-space: nowrap;
  }
  .brand-mark { background: var(--navy); flex: none; }

  .headline { font-weight: 800; line-height: 1; white-space: nowrap; }
  .headline .dark { color: var(--ink); display: block; }
  .headline .accent { color: var(--orange); font-weight: 900; display: block; }

  .offer { color: var(--white); white-space: nowrap; line-height: 1.15; }
  .offer .light { font-weight: 400; }
  .offer .hot { color: var(--orange); font-weight: 700; }
  .offer .bold { font-weight: 800; }
</style>
</head>
<body>

<!-- Square feed banner -->
<section class="banner banner--square">
  <div class="abs town-photo" style="left:0;top:0;width:580px;height:274px" role="img" aria-label="Photo of St. John's hillside with colourful row houses and a twin-towered basilica under a grey sky"></div>

  <div class="abs brand" style="left:0;width:580px;top:43px;justify-content:center;font-size:16px">
    <span class="brand-mark" style="width:14px;height:14px"></span>
    Bright Harbour Mortgages
  </div>

  <div class="abs grey-panel" style="left:0;top:274px;width:178px;height:306px"></div>
  <div class="abs navy-band" style="left:178px;top:465px;width:402px;height:115px"></div>
  <svg class="roof" width="580" height="580" viewBox="0 0 580 580" aria-hidden="true">
    <polygon fill="var(--navy)" points="37,274 95,235 227,315 227,343 203,329 203,466 178,466 178,309 135,274"/>
  </svg>

  <div class="abs agent-photo" style="left:15px;top:245px;width:148px;height:175px" role="img" aria-label="Portrait photo of the mortgage agent"></div>
  <div class="abs name-bar" style="left:15px;top:420px;width:148px;height:23px;font-size:13px;line-height:23px">MAREN HOLLOWAY</div>
  <div class="abs contact-card" style="left:15px;top:443px;width:148px;height:104px;padding:6px 0 6px">
    <svg class="contact-icon" width="36" height="12" viewBox="0 0 36 12" aria-hidden="true"><g fill="none" stroke="#fff" stroke-width="1.1"><path d="M2 6h5M29 6h5"/><path d="M13 2.5c-1 1 0 4 2.5 6.5s5 3.5 6 2.5l1-1-2-2-1.3 1c-1-.3-3.5-2.8-3.8-3.8l1-1.3-2-2z"/></g></svg>
    <div class="contact-phone" style="font-size:10px">709-555-0148</div>
    <svg class="contact-icon" width="36" height="12" viewBox="0 0 36 12" aria-hidden="true"><g fill="none" stroke="#fff" stroke-width="1.1"><path d="M2 6h5M29 6h5"/><rect x="13" y="2.5" width="11" height="7.5"/><path d="M13 2.5l5.5 4.5 5.5-4.5"/></g></svg>
    <div class="contact-text" style="font-size:8.5px">info@capelinemortgages.com</div>
    <svg class="contact-icon" width="36" height="12" viewBox="0 0 36 12" aria-hidden="true"><g fill="none" stroke="#fff" stroke-width="1.1"><path d="M2 6h5M29 6h5"/><circle cx="18" cy="6" r="5"/><ellipse cx="18" cy="6" rx="2.2" ry="5"/><path d="M13 6h10"/></g></svg>
    <div class="contact-text" style="font-size:8.5px">www.capelinemortgages.com</div>
  </div>

  <h1 class="abs headline" style="left:245px;top:310px">
    <span class="dark" style="font-size:26px;font-weight:700">BUILDING YOUR</span>
    <span class="dark" style="font-size:34px;margin-top:4px">DREAM HOME,</span>
    <span class="accent" style="font-size:32px;margin-top:8px">ONE MORTGAGE</span>
    <span class="accent" style="font-size:32px;margin-top:3px">AT A TIME</span>
  </h1>

  <p class="abs offer" style="left:243px;top:484px;font-size:17px">
    <span class="light">Let Us Help You</span> <span class="hot">Unlock Your</span><br>
    <span class="hot">DREAM HOME TODAY</span> <span class="light">With</span><br>
    <span class="bold" style="font-size:22px">Low Rates</span> <span class="light" style="font-size:20px">&amp;</span> <span class="bold" style="font-size:22px">Great Deals!</span>
  </p>
</section>

<!-- Wide link banner -->
<section class="banner banner--wide">
  <div class="abs grey-panel" style="left:0;top:0;width:174px;height:304px"></div>
  <div class="abs town-photo" style="left:200px;top:0;width:380px;height:139px" role="img" aria-label="Photo of St. John's hillside with colourful row houses and a twin-towered basilica"></div>
  <div class="abs navy-band" style="left:174px;top:244px;width:406px;height:60px"></div>
  <svg class="roof" width="580" height="304" viewBox="0 0 580 304" aria-hidden="true">
    <polygon fill="var(--white)" points="227,139 270,124 314,139"/>
    <polygon fill="var(--navy)" points="127,0 224,52 224,66 200,53 200,245 174,245 174,0"/>
  </svg>

  <div class="abs agent-photo" style="left:17px;top:9px;width:134px;height:161px" role="img" aria-label="Portrait photo of the mortgage agent"></div>
  <div class="abs name-bar" style="left:17px;top:170px;width:134px;height:21px;font-size:12px;line-height:21px">MAREN HOLLOWAY</div>
  <div class="abs contact-card" style="left:17px;top:191px;width:134px;height:93px;padding:5px 0">
    <svg class="contact-icon" width="32" height="11" viewBox="0 0 36 12" aria-hidden="true"><g fill="none" stroke="#fff" stroke-width="1.1"><path d="M2 6h5M29 6h5"/><path d="M13 2.5c-1 1 0 4 2.5 6.5s5 3.5 6 2.5l1-1-2-2-1.3 1c-1-.3-3.5-2.8-3.8-3.8l1-1.3-2-2z"/></g></svg>
    <div class="contact-phone" style="font-size:9px">709-555-0148</div>
    <svg class="contact-icon" width="32" height="11" viewBox="0 0 36 12" aria-hidden="true"><g fill="none" stroke="#fff" stroke-width="1.1"><path d="M2 6h5M29 6h5"/><rect x="13" y="2.5" width="11" height="7.5"/><path d="M13 2.5l5.5 4.5 5.5-4.5"/></g></svg>
    <div class="contact-text" style="font-size:7.8px">info@capelinemortgages.com</div>
    <svg class="contact-icon" width="32" height="11" viewBox="0 0 36 12" aria-hidden="true"><g fill="none" stroke="#fff" stroke-width="1.1"><path d="M2 6h5M29 6h5"/><circle cx="18" cy="6" r="5"/><ellipse cx="18" cy="6" rx="2.2" ry="5"/><path d="M13 6h10"/></g></svg>
    <div class="contact-text" style="font-size:7.8px">www.capelinemortgages.com</div>
  </div>

  <div class="abs brand" style="left:228px;top:157px;font-size:13px;gap:6px">
    <span class="brand-mark" style="width:12px;height:12px"></span>
    Bright Harbour Mortgages
  </div>

  <h2 class="abs headline" style="left:228px;top:195px">
    <span class="dark" style="font-size:18.5px">BUILDING YOUR DREAM HOME,</span>
    <span class="accent" style="font-size:20px;margin-top:2px">ONE MORTGAGE AT A TIME</span>
  </h2>

  <p class="abs offer" style="left:228px;top:254px;font-size:12px">
    <span class="light">Let Us Help You</span> <span class="hot">Unlock Your DREAM HOME TODAY</span><br>
    <span class="light">With</span> <span class="bold" style="font-size:14px">Low Rates</span> <span class="light">&amp;</span> <span class="bold" style="font-size:14px">Great Deal</span>
  </p>
</section>

</body>
</html>
```